Launching a consulting business

I need a business card to launch a new consulting business. I provide executive level consultation throughout New York state to CEO and ED's who run and manage non-fo-profit corporations who support individuals with intellectual and developmental disabilities. The field is undergoing an evolution from a social model of care to more outcome based strategies. Having expertise in health care, leading a $50M business providing this service and working in the government creating policy I can bring to the Executive and corporations compassion, vision, strategy with a clear understanding of business practices for success. The field is moving to managed care. My background in health care management brings the expertise to create opportunities and possibilities. I currently have three projects I am consulting on - 1. Field expert assisting an accounting firm in the creation of a managed care application to become a managed care company supporting the ID/DD field. I crafted the care management model 2. Strategizing on product line creation to assure an agency is ready with a compendium services supporting the ID/DD field. 3. Facilitating a financial model to assist in predicting costs to render services in ID/DD. Developing and overlaying outcome measures to position agencies for effective marketing.
Quality is my passion and assuring all people live their life's dreams.
I would also like a template for letterhead stationary following what is created with my business card.
I wold like to incorporate a cranberry/sage tartan plaid within the design.

Please note my last name is spelled wrong on the attachment. I also do not want the tartan plaid used covering the entire card. i open to other ideas and suggestions.

Industry/Entity Type

Government

Contact Information for Business Card

Donna M Farris
Phone - 845-620-4178
Cell phone 845-733-2906
Email address - donnamfar@quillmail.com

```html
<!DOCTYPE html>
<html lang="en">
<head>
<meta charset="utf-8">
<title>Donna M Farris — Business Card</title>
<link rel="stylesheet" href="https://fonts.googleapis.com/css2?family=Tinos:wght@400;700&display=swap">
<style>
  :root {
    --sage-dark: #7aae92;
    --sage-light: #c6e3d4;
    --card-white: #ffffff;
    --ink: #1c1c1c;
    --name-green: #74ab8d;
    --backdrop: #ecebe7;
  }
  * { margin: 0; padding: 0; box-sizing: border-box; }
  html, body {
    width: 1200px; height: 848px; overflow: hidden;
    background: var(--backdrop);
    font-family: "Tinos", "Times New Roman", serif;
  }
  .sheet {
    width: 1200px; height: 848px;
    display: flex; flex-direction: column;
    align-items: center; justify-content: center; gap: 56px;
  }
  .card {
    position: relative;
    width: 620px; height: 354px;
    background: var(--card-white);
    box-shadow: 0 6px 18px rgba(0,0,0,0.14);
    overflow: hidden;
  }
  .band { position: absolute; left: 0; right: 0; }
  .band--dark-top { top: 0; height: 20px; background: var(--sage-dark); }
  .band--light-top { top: 27px; height: 22px; background: var(--sage-light); }
  .band--light-bottom { bottom: 27px; height: 22px; background: var(--sage-light); }
  .band--dark-bottom { bottom: 0; height: 20px; background: var(--sage-dark); }

  .identity { position: absolute; left: 0; right: 0; text-align: center; }
  .identity__name {
    font-variant: small-caps;
    color: var(--name-green);
    font-weight: 400;
    letter-spacing: 1px;
    line-height: 1;
  }
  .identity__title { color: var(--ink); line-height: 1.2; }

  .card--front .identity { top: 82px; }
  .card--front .identity__name { font-size: 52px; }
  .card--front .identity__title { font-size: 19px; margin-top: 4px; }

  .card--back .identity { top: 128px; }
  .card--back .identity__name { font-size: 60px; }
  .card--back .identity__title { font-size: 21px; margin-top: 4px; }

  .contact {
    position: absolute; top: 192px; left: 236px;
    list-style: none;
  }
  .contact__item {
    display: flex; align-items: center; gap: 12px;
    height: 30px; font-size: 18px; color: var(--ink);
  }
  .contact__item--email { font-variant: small-caps; font-weight: 700; font-size: 16px; letter-spacing: 0.3px; }
  .contact__icon { width: 20px; height: 18px; flex: none; }
</style>
</head>
<body>
<main class="sheet">

  <section class="card card--front" aria-label="Business card front">
    <div class="band band--dark-top"></div>
    <div class="band band--light-top"></div>
    <div class="identity">
      <h1 class="identity__name">Donna M Farris</h1>
      <p class="identity__title">Executive Business Strategy Consultant</p>
    </div>
    <ul class="contact">
      <li class="contact__item">
        <svg class="contact__icon" viewBox="0 0 20 18" aria-hidden="true">
          <path d="M2 6 Q10 0 18 6 L16 8 L13 6.5 L13 4.5 Q10 3.5 7 4.5 L7 6.5 L4 8 Z" fill="var(--sage-dark)"/>
          <path d="M5 9 L15 9 L17 16 L3 16 Z" fill="var(--sage-dark)"/>
          <circle cx="10" cy="12.5" r="2" fill="var(--card-white)"/>
        </svg>
        <span>845-620-4178</span>
      </li>
      <li class="contact__item">
        <svg class="contact__icon" viewBox="0 0 20 18" aria-hidden="true">
          <rect x="6" y="0.5" width="8" height="17" rx="1.5" fill="none" stroke="var(--sage-dark)" stroke-width="1.4"/>
          <rect x="7.5" y="2.5" width="5" height="6" fill="var(--sage-light)"/>
          <rect x="7.5" y="10.5" width="5" height="5" fill="var(--sage-dark)" opacity="0.6"/>
        </svg>
        <span>845-733-2906</span>
      </li>
      <li class="contact__item contact__item--email">
        <svg class="contact__icon" viewBox="0 0 20 18" aria-hidden="true">
          <rect x="1" y="3" width="18" height="12" fill="var(--sage-dark)"/>
          <path d="M1 3 L10 10 L19 3" fill="none" stroke="var(--card-white)" stroke-width="1.2"/>
        </svg>
        <span>donnamfar@quillmail.com</span>
      </li>
    </ul>
    <div class="band band--light-bottom"></div>
    <div class="band band--dark-bottom"></div>
  </section>

  <section class="card card--back" aria-label="Business card back">
    <div class="band band--dark-top"></div>
    <div class="band band--light-top"></div>
    <div class="identity">
      <h2 class="identity__name">Donna M Farris</h2>
      <p class="identity__title">Executive Business Strategy Consultant</p>
    </div>
    <div class="band band--light-bottom"></div>
    <div class="band band--dark-bottom"></div>
  </section>

</main>
</body>
</html>
```